TEK Logistics - Banner 2.5' x 8' for 20+ locations

Need a banner designed that will pop. This banner will be displayed at over 20 of our transportation facilities. Goal is for the banner to grab the attention of employees, contractors and clients and help reinforce our mission and core values. Designed needs to include TEK Logo, our core values and mission statement. Red and Black are the main company colors and we need to stay within that theme and color pallet. Attached is a previous version that was too basic and boring. Willing to consider a design that excludes the mission statement.

Gathering more feedback

```html
<!DOCTYPE html>
<html lang="en">
<head>
<meta charset="utf-8">
<title>TEK Logistics – Core Values Banner</title>
<link rel="stylesheet" href="https://fonts.googleapis.com/css2?family=Exo+2:wght@700&family=Montserrat:wght@700&display=swap">
<style>
  :root {
    --brand-red: #d42a2a;
    --brand-red-dark: #a51c1c;
    --field-dark: #141414;
    --field-mid: #2a2a2a;
    --ink: #2b2b2b;
    --paper: #ffffff;
    --text-light: #ffffff;
  }
  html, body {
    margin: 0;
    padding: 0;
    overflow: hidden;
    background: var(--paper);
  }
  .banner {
    position: relative;
    width: 1200px;
    height: 375px;
    overflow: hidden;
    background: var(--paper);
  }
  .banner__shapes {
    position: absolute;
    inset: 0;
  }
  .brand {
    position: absolute;
    left: 15px;
    top: 68px;
    display: flex;
    align-items: center;
    gap: 12px;
    font-family: "Exo 2", sans-serif;
    font-weight: 700;
    color: var(--brand-red);
  }
  .brand__dot {
    width: 18px;
    height: 18px;
    border-radius: 50%;
    background: var(--brand-red);
  }
  .brand__name {
    display: flex;
    flex-direction: column;
    line-height: 1;
  }
  .brand__name-main {
    font-size: 60px;
    letter-spacing: 4px;
  }
  .brand__name-sub {
    font-size: 22px;
    letter-spacing: 7px;
    margin-top: 2px;
  }
  .values {
    margin: 0;
    padding: 0;
    list-style: none;
    font-family: "Exo 2", sans-serif;
    font-weight: 700;
    color: var(--text-light);
    font-size: 30px;
    line-height: 1;
  }
  .values__item {
    position: absolute;
    white-space: nowrap;
  }
  .values__item::before {
    content: "•";
    margin-right: 16px;
  }
  .values__item--1 { left: 452px; top: 40px; }
  .values__item--2 { left: 405px; top: 92px; }
  .values__item--3 { left: 359px; top: 145px; }
  .values__item--4 { left: 318px; top: 197px; }
  .values__item--5 { left: 266px; top: 250px; }
  .values__item--6 { left: 817px; top: 250px; }
  .mission {
    position: absolute;
    left: 110px;
    width: 960px;
    top: 323px;
    margin: 0;
    text-align: center;
    font-family: "Montserrat", sans-serif;
    font-weight: 700;
    font-size: 16px;
    line-height: 20px;
    color: var(--text-light);
  }
</style>
</head>
<body>
<div class="banner">
  <svg class="banner__shapes" width="1200" height="375" viewBox="0 0 1200 375">
    <defs>
      <linearGradient id="fieldTone" x1="0" y1="0" x2="1" y2="1">
        <stop offset="0" stop-color="var(--field-mid)"/>
        <stop offset="1" stop-color="var(--field-dark)"/>
      </linearGradient>
      <linearGradient id="redEdge" x1="0" y1="0" x2="1" y2="1">
        <stop offset="0" stop-color="#e23a3a"/>
        <stop offset="1" stop-color="#9e1a1a"/>
      </linearGradient>
    </defs>
    <path class="value-field" role="img" aria-label="Dark textured background behind the core values"
          d="M490,0 L1200,0 L1200,185 Q1170,290 1120,375 L75,375 Q230,130 490,0 Z"
          fill="url(#fieldTone)"/>
    <path class="mission-band" d="M95,297 L1200,322 L1200,375 L55,375 Z" fill="var(--brand-red-dark)"/>
    <path class="edge-left" d="M470,0 L492,0 Q232,130 77,375 L58,375 Q210,125 470,0 Z" fill="url(#redEdge)"/>
    <path class="edge-right" d="M1200,178 L1200,196 Q1175,295 1128,375 L1112,375 Q1165,285 1200,178 Z" fill="url(#redEdge)"/>
    <path class="white-corner" d="M1200,196 Q1175,295 1128,375 L1200,375 Z" fill="var(--paper)"/>
  </svg>

  <div class="brand">
    <div class="brand__name">
      <span class="brand__name-main">TEK</span>
      <span class="brand__name-sub">LOGISTICS</span>
    </div>
    <span class="brand__dot"></span>
  </div>

  <ul class="values">
    <li class="values__item values__item--1">Do the right things for the right reasons</li>
    <li class="values__item values__item--2">Pursue growth and development</li>
    <li class="values__item values__item--3">Build a positive team atmosphere</li>
    <li class="values__item values__item--4">Deliver WOW through service</li>
    <li class="values__item values__item--5">Do Everything Safety</li>
    <li class="values__item values__item--6">HAVE FUN</li>
  </ul>

  <p class="mission">Provide the best customer experience while creating an environment of growth and opportunity<br>for our customers, employees, and service providers.</p>
</div>
</body>
</html>
```